1300 Cratelofn Van wrap

We are forklift mechanics.
Design a simple wrap to suit our 4 vans with our logo.
Add some colour/design using the base colours happy to add other colours as suits and highlights/shadows to balance/break up the white but not over power it.
Include mobile number 0491 570 266

```html
<!DOCTYPE html>
<html lang="en">
<head>
<meta charset="utf-8">
<title>1300 Cratelofn Van Wrap</title>
<link rel="stylesheet" href="https://fonts.googleapis.com/css2?family=Anton&family=Oswald:wght@600&family=Montserrat:wght@700;800&display=swap">
<style>
  :root {
    --wrap-red: #d8232a;
    --wrap-black: #111111;
    --wrap-white: #ffffff;
    --canvas-bg: #f1f1f1;
  }
  html, body {
    margin: 0;
    padding: 0;
    width: 1200px;
    height: 900px;
    overflow: hidden;
    background: var(--canvas-bg);
  }
  .wrap-artboard {
    display: block;
    width: 1200px;
    height: 900px;
  }
  .panel-base { fill: var(--wrap-white); }
  .panel-red { fill: var(--wrap-red); }
  .panel-black { fill: var(--wrap-black); }
  .panel-stripe { fill: var(--wrap-white); }
  .brand-name {
    font-family: "Anton", "Oswald", sans-serif;
    font-size: 104px;
    fill: var(--wrap-white);
    letter-spacing: 1px;
  }
  .mobile-number {
    font-family: "Montserrat", sans-serif;
    font-weight: 800;
    font-size: 29px;
    fill: var(--wrap-black);
    letter-spacing: 1px;
  }
  .service-line {
    font-family: "Oswald", sans-serif;
    font-weight: 600;
    font-size: 21px;
    fill: var(--wrap-white);
  }
  .web-address {
    font-family: "Montserrat", sans-serif;
    font-weight: 700;
    font-size: 19px;
    fill: var(--wrap-black);
  }
</style>
</head>
<body>
<svg class="wrap-artboard" viewBox="0 0 1200 900" xmlns="http://www.w3.org/2000/svg" aria-label="Van side wrap layout">
  <rect class="panel-base" x="20" y="200" width="1160" height="420" rx="22"/>

  <polygon class="panel-red" points="30,212 378,208 470,418 680,418 680,530 330,530 330,560 30,560"/>

  <rect class="panel-stripe" x="30" y="238" width="320" height="14"/>
  <rect class="panel-stripe" x="80" y="262" width="210" height="80"/>
  <polygon class="panel-stripe" points="45,358 332,358 296,400 45,400"/>
  <rect class="panel-stripe" x="30" y="445" width="72" height="20"/>
  <rect class="panel-stripe" x="30" y="505" width="72" height="20"/>

  <polygon class="panel-black" points="370,208 408,208 492,418 456,418"/>

  <rect class="panel-black" x="350" y="415" width="420" height="8"/>
  <polygon class="panel-black" points="742,418 1114,418 1100,446 730,446"/>

  <polygon class="panel-black" points="330,527 444,527 424,562 330,562"/>

  <polygon class="panel-black" points="742,418 778,418 684,618 646,618"/>

  <polygon class="panel-red" points="744,478 1052,480 1032,506 732,506"/>

  <text class="mobile-number" x="56" y="390">0491 570 266</text>
  <text class="brand-name" x="108" y="520" textLength="560" lengthAdjust="spacingAndGlyphs">1300 CRATELOFN</text>
  <text class="service-line" x="776" y="441" textLength="308" lengthAdjust="spacingAndGlyphs">HIRE - SALES - SERVICE - REPAIRS</text>
  <text class="web-address" x="776" y="471" textLength="306" lengthAdjust="spacingAndGlyphs">WWW.1300CRATELOFN.COM.AU</text>
</svg>
</body>
</html>
```